Business Card Design for an Investment Company

We need a business card design for our private investment company, called Ashbourne Partners. Ashbourne Partners is an investments partnership that aims to acquire shares in listed companies with a view to influencing those companies through active dialogue in order to improve their value. We need designs that use the logo colors (blue, grey, white), we need both English and Arabic on the business cards (can be on one side or 2 sides). The final logo should communicate professionalism, conservatism (nothing too fancy or too cheesy), that we are smart, conservative and old school.

Target Market(s)

Investment companies

Industry/Entity Type

Investment

Contact Information for Business Card

Khalid Yousef Rumaithi
Senior Executive Officer

Palm Terrace 07, Level 3, Office 215/12
HLMZ

+9714987650
krumaithi@ashbournepartners.com
www.ashbournepartners.com

Requirements
Must have
• Logo to be placed on the left hand side of the business card
• for the Arabic, we only need to have the name and title so it can be accomodated on one side so we can have the other side with full color and logo. The arabic that needs to be used is the below:
• خالد يوسف الرميثي
• المدير التنفيدي

```html
<!DOCTYPE html>
<html lang="en">
<head>
<meta charset="utf-8">
<title>Ashbourne Partners – Business Card</title>
<link href="https://fonts.googleapis.com/css2?family=Open+Sans:wght@400;700&family=Noto+Naskh+Arabic:wght@400&display=swap" rel="stylesheet">
<style>
  :root {
    --brand-blue: #1f6fa8;
    --label-blue: #1c5f96;
    --brand-grey: #58585a;
    --text-grey: #555557;
    --card-white: #ffffff;
    --backdrop: #e9e7e4;
  }
  * { margin: 0; padding: 0; box-sizing: border-box; }
  html, body {
    width: 1200px; height: 1000px; overflow: hidden;
    background: var(--backdrop);
  }
  .canvas { position: relative; width: 1200px; height: 1000px; }
  .card {
    position: absolute; left: 266px; width: 666px; height: 397px;
    background: var(--card-white);
    box-shadow: 0 2px 8px rgba(0,0,0,0.12);
    font-family: "Open Sans", Arial, sans-serif;
  }
  .card--front { top: 74px; }
  .card--back { top: 533px; }

  .wordmark {
    position: absolute; display: flex; align-items: center;
    font-family: "Open Sans", Arial, sans-serif;
    font-weight: 700; color: var(--brand-blue);
    white-space: nowrap; letter-spacing: -0.5px;
  }
  .wordmark__square { background: var(--brand-grey); flex: none; }
  .card--front .wordmark { left: 32px; top: 176px; font-size: 25px; gap: 10px; }
  .card--front .wordmark__square { width: 22px; height: 22px; }
  .card--back .wordmark { left: 0; right: 0; top: 166px; justify-content: center; font-size: 50px; gap: 18px; }
  .card--back .wordmark__square { width: 44px; height: 44px; }

  .contact { position: absolute; left: 347px; top: 78px; color: var(--text-grey); }
  .contact__name { font-size: 17px; color: var(--label-blue); line-height: 22px; }
  .contact__title { font-size: 16px; line-height: 24px; }
  .contact__arabic {
    font-family: "Noto Naskh Arabic", serif; font-size: 15px;
    line-height: 24px; direction: rtl; text-align: left; unicode-bidi: plaintext;
  }
  .contact__arabic--name { color: var(--label-blue); margin-top: 4px; }
  .contact__address { font-size: 16px; line-height: 22px; margin-top: 18px; }
  .contact__lines { margin-top: 9px; font-size: 16px; line-height: 24px; }
  .contact__label { color: var(--label-blue); }
</style>
</head>
<body>
<div class="canvas">
  <section class="card card--front">
    <div class="wordmark"><span class="wordmark__square"></span>Ashbourne Partners</div>
    <div class="contact">
      <p class="contact__name">Khalid Yousef Rumaithi</p>
      <p class="contact__title">Senior Executive Officer</p>
      <p class="contact__arabic contact__arabic--name" lang="ar">خالد يوسف الرميثي</p>
      <p class="contact__arabic" lang="ar">المدير التنفيدي</p>
      <p class="contact__address">Palm Terrace 07, Level 3, Office<br>215/12&nbsp; HLMZ</p>
      <div class="contact__lines">
        <p><span class="contact__label">Phone:</span> +9714987650</p>
        <p><span class="contact__label">Email:</span> krumaithi@ashbournepartners.com</p>
        <p><span class="contact__label">Website:</span> www.ashbournepartners.com</p>
      </div>
    </div>
  </section>
  <section class="card card--back">
    <div class="wordmark"><span class="wordmark__square"></span>Ashbourne Partners</div>
  </section>
</div>
</body>
</html>
```